PowerPoint Template Design for Cobalt Lending

Design a PowerPoint template for Cobalt Lending, tailored for presentations to sophisticated mortgage servicing investors. The template should reflect a high level of professionalism, with a clean and modern aesthetic that resonates with an informed and discerning audience. The design must effectively integrate Cobalt Lending's branding elements, ensuring a coherent visual narrative that reinforces our reputation for expertise and reliability in the mortgage servicing sector.

```html
<!DOCTYPE html>
<html lang="en">
<head>
<meta charset="utf-8">
<title>Cobalt Lending – Presentation Template</title>
<link rel="stylesheet" href="https://fonts.googleapis.com/css2?family=Montserrat:wght@400;500&family=Roboto:wght@300;400;500;700&display=swap">
<style>
  :root{
    --teal:#12abaa;
    --teal-dark:#0f9a99;
    --teal-soft:#8ad6d3;
    --teal-mid:#5cc3c0;
    --ink:#3c3c3c;
    --muted:#8a8a8a;
    --faint:#c4c4c4;
    --paper:#ffffff;
    --canvas-top:#eef1f4;
    --canvas-bottom:#e6eaee;
  }
  *{box-sizing:border-box;margin:0;padding:0}
  html,body{width:914px;height:1200px;overflow:hidden}
  body{background:linear-gradient(180deg,var(--canvas-top),var(--canvas-bottom));font-family:"Roboto",Arial,sans-serif;color:var(--ink);position:relative}
  .slide{position:absolute;width:272px;height:153px;background:var(--paper);overflow:hidden;box-shadow:0 6px 14px rgba(60,70,80,.22)}
  .abs{position:absolute}
  .photo{position:absolute}
  .display{font-family:"Montserrat",Arial,sans-serif;font-weight:400;color:var(--teal);letter-spacing:1px;line-height:1.15}
  .light-title{font-family:"Roboto",Arial,sans-serif;font-weight:300;color:var(--teal);text-align:center;width:100%;left:0}
  .sub{font-size:3.4px;color:var(--faint);text-align:center;width:100%;left:0}
  .body-text{font-size:3.6px;line-height:1.85;color:#333}
  .small-grey{font-size:2.9px;line-height:1.35;color:var(--muted)}
  .teal-caps{font-size:4.2px;color:var(--teal);font-weight:500}
  .num-dot{position:absolute;border-radius:50%;background:var(--teal);color:#fff;font-size:4px;font-weight:700;display:flex;align-items:center;justify-content:center}
  .data-table{border-collapse:collapse;width:100%;font-size:2.7px;color:#777;text-align:center}
  .data-table th{background:var(--teal);color:#fff;font-weight:400;height:9.5px;border:.3px solid #fff}
  .data-table td{height:7.6px;border-bottom:.3px solid #e4e4e4}
  .data-table tr:nth-child(odd) td{background:#f2f2f2}
  .data-table td:first-child{text-align:left;padding-left:5px}
  .adv-card{position:absolute;top:56px;width:45px;height:84px;background:linear-gradient(180deg,var(--teal-mid),var(--teal-soft));border-top:2px solid var(--teal);color:#fff;text-align:center}
  .adv-card h4{font-size:3.8px;font-weight:400;margin-top:3px}
  .adv-card p{font-size:2.6px;line-height:1.3;padding:3px 4px 0;opacity:.95}
  .adv-card svg{margin-top:9px}
</style>
</head>
<body>

<!-- Centre 1: two-column text with house -->
<section class="slide" style="left:321px;top:65px">
  <div class="photo" role="img" aria-label="Photo of a modern white two-storey house with wood accent" style="left:11px;top:18px;width:85px;height:98px;background:linear-gradient(180deg,#c9d3dc 0%,#e6e6e4 45%,#9e9a92 80%,#6f8a52 100%)"></div>
  <div class="abs" style="left:106px;top:27px;width:107px;height:.7px;background:var(--teal)"></div>
  <div class="abs" style="left:106px;top:34px;width:51px;height:.7px;background:var(--teal)"></div>
  <div class="abs display" style="left:107px;top:51px;font-size:7px">DOLOR SIT AMET</div>
  <p class="abs body-text" style="left:107px;top:72px;width:68px">Lorem ipsum dolor sit amet, consectetuer adipiscing elit, sed diam nonummy nibh euismod tincidunt ut laoreet dolore magna aliquam erat volutpat. Ut wisi enim ad minim veniam, quis nostrud exerci tation ullamcorper.</p>
  <div class="abs display" style="left:188px;top:76px;font-size:7px">DOLOR SIT AMET</div>
  <p class="abs body-text" style="left:188px;top:88px;width:68px">Lorem ipsum dolor sit amet, consectetuer adipiscing elit, sed diam nonummy nibh euismod tincidunt ut laoreet dolore magna aliquam erat volutpat. Ut wisi enim ad minim veniam, quis nostrud exerci tation ullamcorper.</p>
</section>

<!-- Left 1: diagonal interior cover -->
<section class="slide" style="left:16px;top:185px">
  <div class="photo" role="img" aria-label="Photo of a bright modern living room with wood ceiling and wall TV" style="inset:0;background:linear-gradient(120deg,#e9e3da 0%,#d9d4cc 40%,#8a8884 70%,#b9aa96 100%)"></div>
  <svg class="abs" style="left:0;top:0" width="272" height="153" viewBox="0 0 272 153"><polygon points="0,0 50,0 272,153 0,153" fill="#fff"/></svg>
  <h1 class="abs display" style="left:13px;top:44px;font-size:13.5px">Lorem<br>Ipsum sit</h1>
  <div class="abs" style="left:13px;top:79px;width:63px;height:.6px;background:var(--teal)"></div>
  <p class="abs body-text" style="left:14px;top:91px;width:135px;line-height:1.6;font-size:4.2px">Lorem ipsum dolor sit amet, consectetuer adipiscing elit, sed diam nonummy nibh euismod tincidunt ut laoreet dolore magna</p>
  <p class="abs body-text" style="left:14px;top:120px;width:180px;line-height:1.6;font-size:4.2px">Lorem ipsum dolor sit amet, consectetuer adipiscing elit, sed diam nonummy nibh euismod tincidunt ut laoreet dolore magna</p>
</section>

<!-- Right 1: teal band with villa -->
<section class="slide" style="left:626px;top:184px">
  <div class="abs" style="left:0;top:0;width:97px;height:153px;background:var(--teal)"></div>
  <div class="photo" role="img" aria-label="Photo of a white modern villa with a swimming pool" style="left:22px;top:16px;width:140px;height:121px;background:linear-gradient(180deg,#3f6fa8 0%,#9fb9d4 38%,#dcdcd6 55%,#3b7f9c 78%,#2a5f78 100%)"></div>
  <h2 class="abs display" style="right:14px;top:23px;font-size:13.5px;text-align:right">Lorem<br>ipsum dolor</h2>
  <p class="abs body-text" style="right:14px;top:60px;width:82px;text-align:right;line-height:1.75;font-size:4.1px">Lorem ipsum dolor sit amet, cons ectetuer adipiscing elit, sed diam nonummy nibh euismod tincidunt ut laoreet dolore magna aliquam erat volutpat. Ut wisi enim ad minim veniam. elit, sed diam nonummy nibh euismod tincidunt ut laoreet dolore . Lorem ipsum dolor sit amet, cons ectetuer adipiscing elit,</p>
</section>

<!-- Centre 2: four-photo grid -->
<section class="slide" style="left:321px;top:259px">
  <div class="abs" style="left:215px;top:0;width:57px;height:153px;background:var(--teal)"></div>
  <h2 class="abs display" style="left:19px;top:23px;font-size:13.5px">Lorem<br>Ipsum dolor</h2>
  <p class="abs body-text" style="left:19px;top:62px;width:82px;font-size:3.5px;line-height:2">Lorem ipsum dolor sit amet, cons ectetuer adipiscing elit, sed diam nonummy nibh euismod tincidunt ut laoreet dolore magna aliquam erat volutpat. Ut wisi enim ad minim veniam. elit, sed diam nonummy nibh euismod tincidunt ut laoreet dolore . Lorem ipsum dolor sit amet, cons ectetuer adipiscing elit,</p>
  <p class="abs body-text" style="left:19px;top:119px;width:82px;font-size:3.5px;line-height:2">Lorem ipsum dolor sit amet, cons ectetuer adipiscing elit, sed diam nonummy nibh euismod tincidunt ut laoreet dolore magna</p>
  <div class="photo" role="img" aria-label="Photo of a modern apartment block with balconies" style="left:113px;top:17px;width:69px;height:58px;background:linear-gradient(180deg,#9bb8d6,#6f7576 55%,#4f5a4a)"></div>
  <div class="photo" role="img" aria-label="Photo of white stacked apartment balconies" style="left:186px;top:17px;width:69px;height:58px;background:linear-gradient(135deg,#d8d8d8,#f4f4f4 50%,#c2c2c2)"></div>
  <div class="photo" role="img" aria-label="Photo of white stacked apartment balconies" style="left:113px;top:78px;width:69px;height:58px;background:linear-gradient(135deg,#d8d8d8,#f4f4f4 50%,#c2c2c2)"></div>
  <div class="photo" role="img" aria-label="Photo of a modern apartment block with balconies" style="left:186px;top:78px;width:69px;height:58px;background:linear-gradient(180deg,#9bb8d6,#6f7576 55%,#4f5a4a)"></div>
</section>

<!-- Left 2: numbered list with house -->
<section class="slide" style="left:16px;top:380px">
  <div class="photo" role="img" aria-label="Photo of a white family house with gabled roof" style="left:0;top:0;width:160px;height:153px;clip-path:polygon(0 0,63px 0,150px 153px,0 153px);background:linear-gradient(180deg,#b9cde0 0%,#e3e3e0 40%,#a9a39a 75%,#5f8a45 100%)"></div>
  <svg class="abs" style="left:0;top:0" width="272" height="153" viewBox="0 0 272 153">
    <line x1="63" y1="0" x2="150" y2="153" stroke="#12abaa" stroke-width="1.4"/>
    <polygon points="93,70 103,70 150,153 135,153" fill="#12abaa"/>
    <polygon points="115,52 149,52 160,75 126,75" fill="#12abaa"/>
    <polygon points="129,78 163,78 174,101 140,101" fill="#12abaa"/>
    <polygon points="143,106 177,106 188,129 154,129" fill="#12abaa"/>
  </svg>
  <span class="abs" style="left:130px;top:60px;font-size:5px;color:#fff">01</span>
  <span class="abs" style="left:144px;top:86px;font-size:5px;color:#fff">03</span>
  <span class="abs" style="left:158px;top:114px;font-size:5px;color:#fff">04</span>
  <h2 class="abs display" style="right:21px;top:20px;font-size:12.5px">Lorem ipsum dolor</h2>
  <p class="abs body-text" style="left:144px;top:52px;width:110px;font-size:3.3px;line-height:2.1">Lorem ipsumectetuer adipiscing elit, sed diam nonummy nibh euismod tincidunt Lorem ipsumectetuer adipiscing elit, sed diam nonummy nibh euismod</p>
  <p class="abs body-text" style="left:157px;top:80px;width:105px;font-size:3.3px;line-height:2.1">Lorem ipsumectetuer adipiscing elit, sed diam nonummy nibh euismod tincidunt Lorem ipsumectetuer adipiscing elit, sed diam nonummy nibh euismod</p>
  <p class="abs body-text" style="left:171px;top:107px;width:80px;font-size:3.3px;line-height:2.1">Lorem ipsumectetuer adipiscing elit, sed diam nonummy nibh euismod tincidunt Lorem ipsumectetuer adipiscing elit, sed diam.</p>
</section>

<!-- Right 2: numbered titles -->
<section class="slide" style="left:626px;top:381px">
  <h2 class="abs light-title" style="top:10px;font-size:13px">Title goes here</h2>
  <p class="abs sub" style="top:26px">Enter your subhead line here</p>
  <div class="num-dot" style="left:13px;top:48px;width:12px;height:12px">01</div>
  <div class="abs teal-caps" style="left:29px;top:50px">TITLE GOES HERE</div>
  <p class="abs small-grey" style="left:29px;top:56px">This is a sample text. You simply add your own text and description here. This text is fully editable.</p>
  <div class="num-dot" style="left:13px;top:73px;width:12px;height:12px">02</div>
  <div class="abs teal-caps" style="left:29px;top:75px">TITLE GOES HERE</div>
  <p class="abs small-grey" style="left:29px;top:81px">This is a sample text. You simply add your own text and description here. This text is fully editable.</p>
  <div class="num-dot" style="left:13px;top:98px;width:12px;height:12px">03</div>
  <div class="abs teal-caps" style="left:29px;top:100px">TITLE GOES HERE</div>
  <p class="abs small-grey" style="left:29px;top:106px">This is a sample text. You simply add your own text and description here. This text is fully editable.</p>
  <div class="num-dot" style="left:13px;top:123px;width:12px;height:12px">04</div>
  <div class="abs teal-caps" style="left:29px;top:125px">TITLE GOES HERE</div>
  <p class="abs small-grey" style="left:29px;top:131px">This is a sample text. You simply add your own text and description here. This text is fully editable.</p>
</section>

<!-- Centre 3: counters -->
<section class="slide" style="left:321px;top:457px">
  <div class="photo" role="img" aria-label="Photo of a large family house lit at dusk among trees" style="left:0;top:0;width:272px;height:87px;background:linear-gradient(180deg,#2a3446 0%,#4b4e52 45%,#6a5a40 65%,#2f4a2c 100%)"></div>
  <h2 class="abs" style="left:0;width:100%;top:31px;text-align:center;color:#fff;font-weight:300;font-size:13px">Lorem ipsum dolor</h2>
  <p class="abs" style="left:0;width:100%;top:50px;text-align:center;color:#fff;font-weight:300;font-size:7px">Counters Numbers Speak</p>
  <div class="abs" style="left:126px;top:62px;width:20px;height:1px;background:#fff"></div>
  <svg class="abs" style="left:0;top:0" width="272" height="153" viewBox="0 0 272 153">
    <g fill="#12abaa" stroke="#fff" stroke-width="1"><circle cx="53" cy="86" r="11"/><circle cx="109" cy="86" r="11"/><circle cx="164" cy="86" r="11"/><circle cx="220" cy="86" r="11"/></g>
    <g fill="none" stroke="#fff" stroke-width=".8">
      <path d="M48 89 l5-7 l5 3 l-5 6 z M56 82 l2-2"/>
      <rect x="104" y="82" width="10" height="7" transform="rotate(-30 109 86)"/>
      <path d="M159 84 h3 l6-4 v12 l-6-4 h-3 z M161 88 l1 4"/>
      <path d="M214 84 l6-3 l6 3 l-6 3 z M217 86 v3 q3 2 6 0 v-3"/>
    </g>
    <text x="106.5" y="89" font-size="6" fill="#fff" font-family="Roboto">$</text>
  </svg>
  <div class="abs small-grey" style="left:33px;top:104px;width:40px;text-align:center;font-size:3.8px">Company Branches</div>
  <div class="abs small-grey" style="left:89px;top:104px;width:40px;text-align:center;font-size:3.8px">Projects completed</div>
  <div class="abs small-grey" style="left:144px;top:104px;width:40px;text-align:center;font-size:3.8px">Happy clients</div>
  <div class="abs small-grey" style="left:195px;top:104px;width:50px;text-align:center;font-size:3.8px">Year Of Experience</div>
  <div class="abs" style="left:33px;top:112px;width:40px;text-align:center;color:var(--teal);font-weight:700;font-size:12px">60</div>
  <div class="abs" style="left:89px;top:112px;width:40px;text-align:center;color:var(--teal);font-weight:700;font-size:12px">653</div>
  <div class="abs" style="left:139px;top:112px;width:50px;text-align:center;color:var(--teal);font-weight:700;font-size:12px">894 K</div>
  <div class="abs" style="left:200px;top:112px;width:40px;text-align:center;color:var(--teal);font-weight:700;font-size:12px">32</div>
</section>

<!-- Left 3: team with two boxes -->
<section class="slide" style="left:16px;top:576px">
  <div class="photo" role="img" aria-label="Photo of a team gathered around a table in an office" style="left:0;top:0;width:272px;height:64px;background:linear-gradient(90deg,#8f8c88,#c9c2b9 35%,#a9a49e 60%,#6f6b66)"></div>
  <div class="abs" style="left:24px;top:46px;width:102px;height:80px;background:var(--teal-soft);opacity:.95"></div>
  <div class="abs" style="left:147px;top:46px;width:102px;height:80px;background:var(--teal-soft);opacity:.95"></div>
  <div class="abs" style="left:35px;top:52px;font-size:5px;color:#fff">Insert title here</div>
  <div class="abs" style="left:158px;top:52px;font-size:5px;color:#fff">Insert title here</div>
  <p class="abs" style="left:35px;top:73px;width:82px;font-size:3.3px;line-height:1.3;color:#fff">There are many variations of passages of lorem ipsum available, but the majority have suffered alteration in some form, by injected humour. There are many variations of passages of lorem ipsum available, but the majority There are many variations of passages of lorem ipsum available, but the majority</p>
  <p class="abs" style="left:158px;top:73px;width:82px;font-size:3.3px;line-height:1.3;color:#fff">There are many variations of passages of lorem ipsum available, but the majority have suffered alteration in some form, by injected humour. There are many variations of passages of lorem ipsum available, but the majority There are many variations of passages of lorem ipsum available, but the majority</p>
  <p class="abs" style="left:24px;top:133px;width:205px;font-size:3.8px;line-height:1.3;color:var(--teal)">There are many variations of passages of lorem ipsum available, but the majority There are many variations of passages of lorem ipsum available.</p>
</section>

<!-- Right 3: services -->
<section class="slide" style="left:626px;top:576px">
  <h2 class="abs light-title" style="top:10px;font-size:12.5px">Our services</h2>
  <p class="abs sub" style="top:26px">Type the subtitle of your great here</p>
  <div class="abs" style="left:34px;top:45px;width:66px;height:95px;background:var(--teal);box-shadow:0 3px 6px rgba(0,0,0,.2);color:#fff;text-align:center">
    <div style="margin-top:9px;font-size:6px">2023<span style="font-size:3.3px">/ November</span></div>
    <div style="margin-top:6px;font-size:3.5px;line-height:1.4">Insert your amazing<br>statement here.</div>
    <svg width="52" height="40" viewBox="0 0 52 40" style="margin-top:8px">
      <g stroke="#7fd3d1" stroke-width="2.2" stroke-linecap="round"><line x1="5" y1="4" x2="5" y2="34"/><line x1="12" y1="4" x2="12" y2="34"/><line x1="19" y1="4" x2="19" y2="34"/><line x1="26" y1="4" x2="26" y2="34"/><line x1="33" y1="4" x2="33" y2="34"/><line x1="40" y1="4" x2="40" y2="34"/><line x1="47" y1="4" x2="47" y2="34"/></g>
      <g stroke="#fff" stroke-width="2.2" stroke-linecap="round"><line x1="5" y1="14" x2="5" y2="34"/><line x1="12" y1="18" x2="12" y2="34"/><line x1="19" y1="12" x2="19" y2="34"/><line x1="26" y1="16" x2="26" y2="34"/><line x1="33" y1="20" x2="33" y2="34"/><line x1="40" y1="13" x2="40" y2="34"/><line x1="47" y1="9" x2="47" y2="34"/></g>
      <g fill="#fff" font-size="1.8" font-family="Roboto" text-anchor="middle"><text x="5" y="39">Mon</text><text x="12" y="39">Tue</text><text x="19" y="39">Wed</text><text x="26" y="39">Thu</text><text x="33" y="39">Fri</text><text x="40" y="39">Sat</text><text x="47" y="39">Sun</text></g>
    </svg>
  </div>
  <svg class="abs" style="left:96px;top:46px" width="8" height="8" viewBox="0 0 8 8"><circle cx="4" cy="4" r="3.5" fill="#fff"/><path d="M3.2 2.6 L4.6 4 L3.2 5.4" stroke="#12abaa" stroke-width=".7" fill="none"/></svg>
  <div class="abs" style="left:127px;top:45px;width:112px;height:31px;background:#fff;box-shadow:0 2px 6px rgba(0,0,0,.12)"></div>
  <div class="abs" style="left:134px;top:50px;font-size:13px;font-weight:300;color:var(--teal)">01</div>
  <div class="abs" style="left:155px;top:52px;font-size:3.8px;color:var(--teal)">Insert title here</div>
  <p class="abs small-grey" style="left:155px;top:56px;width:65px">There are many variations of passages of lorem ipsum available, but the majority have suffered alteration in some form, by injected humour .</p>
  <div class="abs" style="left:134px;top:87px;font-size:13px;font-weight:300;color:var(--teal)">02</div>
  <div class="abs" style="left:155px;top:89px;font-size:3.8px;color:var(--teal)">Insert title here</div>
  <p class="abs small-grey" style="left:155px;top:93px;width:75px">There are many variations of passages of lorem ipsum available, but the majority have suffered alteration in some form, by injected humour</p>
  <div class="abs" style="left:134px;top:117px;font-size:13px;font-weight:300;color:var(--teal)">03</div>
  <div class="abs" style="left:155px;top:119px;font-size:3.8px;color:var(--teal)">Insert title here</div>
  <p class="abs small-grey" style="left:155px;top:123px;width:75px">There are many variations of passages of lorem ipsum available, but the majority have suffered alteration in some form, by injected humour</p>
</section>

<!-- Centre 4: table -->
<section class="slide" style="left:321px;top:652px">
  <h2 class="abs light-title" style="top:10px;font-size:11.5px">Table</h2>
  <p class="abs sub" style="top:26px">Type the subtitle of your great here</p>
  <div class="abs" style="left:12px;top:48px;width:248px">
    <table class="data-table">
      <thead>
        <tr><th rowspan="2" style="width:52px">Task</th><th colspan="3">Risks</th><th colspan="2">Open</th><th rowspan="2">Pending action</th></tr>
        <tr><th>High</th><th>Medium</th><th>Low</th><th>Issues</th><th>revisions</th></tr>
      </thead>
      <tbody>
        <tr><td>Task 01</td><td>21</td><td>21</td><td>21</td><td>21</td><td>21</td><td>21</td></tr>
        <tr><td>Task 02</td><td>55</td><td>55</td><td>55</td><td>55</td><td>55</td><td>55</td></tr>
        <tr><td>Task 03</td><td>45</td><td>45</td><td>45</td><td>45</td><td>45</td><td>45</td></tr>
        <tr><td>Task 04</td><td>86</td><td>86</td><td>86</td><td>86</td><td>86</td><td>86</td></tr>
        <tr><td>Task 05</td><td>21</td><td>21</td><td>21</td><td>21</td><td>21</td><td>21</td></tr>
        <tr><td>Task 06</td><td>45</td><td>45</td><td>45</td><td>45</td><td>45</td><td>45</td></tr>
        <tr><td>Task 07</td><td>63</td><td>63</td><td>63</td><td>63</td><td>63</td><td>63</td></tr>
        <tr><td>Task 08</td><td>75</td><td>75</td><td>75</td><td>75</td><td>75</td><td>75</td></tr>
        <tr><td>Task 09</td><td>85</td><td>85</td><td>85</td><td>85</td><td>85</td><td>85</td></tr>
        <tr><td>Task 10</td><td>21</td><td>21</td><td>21</td><td>21</td><td>21</td><td>21</td></tr>
        <tr><td>Total</td><td>/</td><td>/</td><td>/</td><td>/</td><td>/</td><td>/</td></tr>
      </tbody>
    </table>
  </div>
</section>

<!-- Left 4: about the company -->
<section class="slide" style="left:13px;top:767px;width:276px;height:155px">
  <div class="photo" role="img" aria-label="Photo of modern apartment buildings along a street" style="left:166px;top:0;width:110px;height:155px;background:linear-gradient(180deg,#a9c3dc 0%,#d9dcdc 35%,#6e6a64 70%,#9a968e 100%)"></div>
  <h2 class="abs" style="left:21px;top:21px;font-size:10.5px;font-weight:300;color:var(--teal);line-height:1.3">What about<br>our company</h2>
  <p class="abs" style="left:21px;top:66px;width:91px;font-size:3.5px;line-height:1.3;color:#999;text-align:justify">There are many variations of passages of Lorem ipsum available, but the majority have suffered alteration in some form, by injected humour, or randomized words which don't look even slightly believable. If you are going to use a passage of Lorem Ipsum, you need to be sure there isn't anything embarrassing hidden in the middle of text.</p>
  <svg class="abs" style="left:21px;top:125px" width="6" height="6" viewBox="0 0 6 6"><circle cx="3" cy="3" r="2.4" fill="none" stroke="#12abaa" stroke-width=".5"/><path d="M.6 3 h4.8 M3 .6 q-1.5 2.4 0 4.8 q1.5-2.4 0-4.8" fill="none" stroke="#12abaa" stroke-width=".4"/></svg>
  <span class="abs" style="left:29px;top:126px;font-size:3.4px;color:var(--teal)">https://www.cobaltlending.example/</span>
  <div class="abs" style="left:125px;top:20px;width:64px;height:116px;background:#fff;box-shadow:0 3px 8px rgba(0,0,0,.15);text-align:center">
    <svg width="18" height="18" viewBox="0 0 18 18" style="margin-top:7px"><g fill="none" stroke="#12abaa" stroke-width=".8"><path d="M2 6 L9 2 L16 6 Z"/><line x1="2" y1="7" x2="16" y2="7"/><line x1="4" y1="8" x2="4" y2="14"/><line x1="7.3" y1="8" x2="7.3" y2="14"/><line x1="10.7" y1="8" x2="10.7" y2="14"/><line x1="14" y1="8" x2="14" y2="14"/><line x1="2" y1="15" x2="16" y2="15"/></g></svg>
    <div style="font-size:4px;color:var(--teal);margin-top:2px">Insert title here</div>
    <p class="small-grey" style="padding:2px 6px 0">There are many variations of passages of lorem ipsum available, but the</p>
    <p class="small-grey" style="padding:4px 6px 0">There are many variations of passages of lorem ipsum available, but the ...</p>
    <p class="small-grey" style="padding:8px 6px 0">There are many variations of passages of lorem ipsum available, but the</p>
    <p class="small-grey" style="padding:8px 6px 0">There are many variations of passages of lorem ipsum available, but the</p>
  </div>
</section>

<!-- Right 4: teal list with house -->
<section class="slide" style="left:626px;top:767px">
  <div class="abs" style="left:0;top:0;width:136px;height:153px;background:var(--teal)"></div>
  <div class="photo" role="img" aria-label="Photo of a white family house with garage under a cloudy sky" style="left:136px;top:0;width:136px;height:153px;background:linear-gradient(180deg,#8fb1d6 0%,#e2e6ea 40%,#bdb7ad 70%,#6f9a4f 100%)"></div>
  <svg class="abs" style="left:121px;top:61px" width="30" height="30" viewBox="0 0 30 30"><circle cx="15" cy="15" r="15" fill="#fff"/><path d="M10 18 h10 a3 3 0 0 0 0-6 a5 5 0 0 0-9.5-1 a3.5 3.5 0 0 0-.5 7z M15 14 v6 M13 18 l2 2 l2-2" fill="none" stroke="#12abaa" stroke-width="1"/></svg>
  <g></g>
  <div class="abs" style="left:11px;top:31px;width:12px;height:12px;border:.7px solid #fff;border-radius:50%;color:#fff;font-size:4px;display:flex;align-items:center;justify-content:center">01</div>
  <div class="abs" style="left:11px;top:56px;width:12px;height:12px;border:.7px solid #fff;border-radius:50%;color:#fff;font-size:4px;display:flex;align-items:center;justify-content:center">02</div>
  <div class="abs" style="left:11px;top:81px;width:12px;height:12px;border:.7px solid #fff;border-radius:50%;color:#fff;font-size:4px;display:flex;align-items:center;justify-content:center">03</div>
  <div class="abs" style="left:11px;top:106px;width:12px;height:12px;border:.7px solid #fff;border-radius:50%;color:#fff;font-size:4px;display:flex;align-items:center;justify-content:center">04</div>
  <div class="abs" style="left:28px;top:31px;font-size:4px;color:#fff">TITLE GOES HERE</div>
  <p class="abs" style="left:28px;top:37px;width:90px;font-size:3px;line-height:1.9;color:#e6f7f7">This is a sample text. You simply add your own text and description here. This text is fully editable.</p>
  <div class="abs" style="left:28px;top:56px;font-size:4px;color:#fff">TITLE GOES HERE</div>
  <p class="abs" style="left:28px;top:62px;width:90px;font-size:3px;line-height:1.9;color:#e6f7f7">This is a sample text. You simply add your own text and description here. This text is fully editable.</p>
  <div class="abs" style="left:28px;top:81px;font-size:4px;color:#fff">TITLE GOES HERE</div>
  <p class="abs" style="left:28px;top:87px;width:90px;font-size:3px;line-height:1.9;color:#e6f7f7">This is a sample text. You simply add your own text and description here. This text is fully editable.</p>
  <div class="abs" style="left:28px;top:106px;font-size:4px;color:#fff">TITLE GOES HERE</div>
  <p class="abs" style="left:28px;top:112px;width:90px;font-size:3px;line-height:1.9;color:#e6f7f7">This is a sample text. You simply add your own text and description here. This text is fully editable.</p>
</section>

<!-- Centre 5: advantages -->
<section class="slide" style="left:321px;top:845px">
  <h2 class="abs light-title" style="top:20px;font-size:13px;font-weight:400">Our advantages</h2>
  <div class="adv-card" style="left:27px">
    <svg width="12" height="12" viewBox="0 0 12 12"><g fill="none" stroke="#fff" stroke-width=".6"><rect x="1" y="1.5" width="10" height="9"/><line x1="1" y1="3.5" x2="11" y2="3.5"/><rect x="2.5" y="5" width="3" height="3"/><line x1="7" y1="5.5" x2="9.5" y2="5.5"/><line x1="7" y1="7.5" x2="9.5" y2="7.5"/></g></svg>
    <h4>Insert title here</h4>
    <p>There are many variations of passages lorem ipsum available, but the majority</p>
    <p style="padding-top:1px">There are many variations of passages lorem ipsum available, but the majority</p>
  </div>
  <div class="adv-card" style="left:85px">
    <svg width="12" height="12" viewBox="0 0 12 12"><path d="M1 5 h3 l5-3 v8 l-5-3 h-3 z M3 7 l1 3 M10.5 4.5 v3" fill="none" stroke="#fff" stroke-width=".6"/></svg>
    <h4>Insert title here</h4>
    <p>There are many variations of passages lorem ipsum available, but the majority</p>
    <p style="padding-top:1px">There are many variations of passages lorem ipsum available, but the majority</p>
  </div>
  <div class="adv-card" style="left:143px">
    <svg width="12" height="12" viewBox="0 0 12 12"><g fill="none" stroke="#fff" stroke-width=".6"><circle cx="4" cy="3" r="1.8"/><circle cx="8" cy="3" r="1.8"/><rect x="2" y="5.5" width="7" height="4"/><path d="M9 6.5 l2-1 v3 l-2-1 M5 9.5 l-1.5 2 M6 9.5 l1.5 2"/></g></svg>
    <h4>Insert title here</h4>
    <p>There are many variations of passages lorem ipsum available, but the majority</p>
    <p style="padding-top:1px">There are many variations of passages lorem ipsum available, but the majority</p>
  </div>
  <div class="adv-card" style="left:200px">
    <svg width="12" height="12" viewBox="0 0 12 12"><g fill="none" stroke="#fff" stroke-width=".6"><circle cx="6" cy="6" r="4.8"/><ellipse cx="6" cy="6" rx="2" ry="4.8"/><line x1="1.2" y1="6" x2="10.8" y2="6"/><line x1="2" y1="3.5" x2="10" y2="3.5"/><line x1="2" y1="8.5" x2="10" y2="8.5"/></g></svg>
    <h4>Insert title here</h4>
    <p>There are many variations of passages lorem ipsum available, but the majority</p>
    <p style="padding-top:1px">There are many variations of passages lorem ipsum available, but the majority</p>
  </div>
</section>

<!-- Centre 6: interior with text columns -->
<section class="slide" style="left:321px;top:1020px">
  <div class="photo" role="img" aria-label="Photo of a sunlit living room with sofa and round coffee table" style="left:0;top:0;width:102px;height:153px;background:linear-gradient(180deg,#6e5a48 0%,#cfc4b4 35%,#e8e1d6 60%,#b9a38a 100%)"></div>
  <div class="abs" style="left:102px;top:0;width:15px;height:153px;background:var(--teal)"></div>
  <h2 class="abs" style="left:129px;top:10px;font-size:12px;font-weight:300;color:var(--teal)">Title here</h2>
  <p class="abs small-grey" style="left:129px;top:40px;width:130px;font-size:3.4px">There are many variations of passages of lorem ipsum available, but the majority have suffered alteration in some form, by injected humour</p>
  <p class="abs small-grey" style="left:129px;top:54px;width:130px;font-size:3.4px">There are many variations of passages of lorem ipsum available, but the majority have suffered alteration in some form, by injected humour</p>
  <div class="abs" style="left:129px;top:83px;font-size:4px;color:var(--teal)">Insert title here</div>
  <div class="abs" style="left:203px;top:83px;font-size:4px;color:var(--teal)">Insert title here</div>
  <p class="abs small-grey" style="left:129px;top:93px;width:46px">There are many variations of passages of lorem ipsum available, but the majority have suffered alteration in some form, by injected humour There are many variations of passages of lorem ipsum available, but the majority</p>
  <p class="abs small-grey" style="left:203px;top:93px;width:46px">There are many variations of passages of lorem ipsum available, but the majority have suffered alteration in some form, by injected humour There are many variations of passages of lorem ipsum available, but the majority</p>
</section>

</body>
</html>
```